BoltCrest Screw Box and Carton Design

We are BoltCrest, a new screw and nail supplier from Ireland. We need box designs branded for our new launch of screws and nails, Outer carton and inner individual boxes. We would like our branding to portray the image of a professional company. We have our logo attached which we would like to stand out so that people recognise the box if it were to be seen from a distance or in a shop.

Target Market(s)

Construction Industry

Industry/Entity Type

Construction

Contact Information for Business Card

Declan Murtagh
Owner
07482619037
declan@boltcrest.co.uk

Font styles to use
Sans Serif

Colors
3277b5

Requirements
Must have
• The Carton should be cost effective for the box maker. The carton will contain 10 boxes. If you could design them in such a way that they can be manipulated easily to cater for the various sizes. The internal boxes that hold the screws will have colour. I like the layout of the Korvex box where the lid folds out over the front of the box. Blue colour #009ee2 Grey colour #4a4a49
Nice to have
• I would like some upgraded design to the original BoltCrest box in the picture. I feel that this design does not cater well for labels or information to be placed on the box.

```html
<!DOCTYPE html>
<html lang="en">
<head>
<meta charset="utf-8">
<title>BoltCrest Screw &amp; Nail Box</title>
<link rel="stylesheet" href="https://fonts.googleapis.com/css2?family=Montserrat:wght@500;800&family=Oswald:wght@600&display=swap">
<style>
  :root {
    --bg: #e6e7ec;
    --panel: #f3f4f6;
    --panel-edge: #d9dbe0;
    --blue: #1b8fd3;
    --blue-deep: #0f7cc0;
    --ink: #232323;
    --white: #ffffff;
    --steel-light: #c9ccd1;
    --steel-dark: #6f747b;
  }
  html, body {
    margin: 0;
    padding: 0;
    width: 1200px;
    height: 1200px;
    overflow: hidden;
    background: var(--bg);
  }
  .box-artwork { display: block; width: 1200px; height: 1200px; }
  .panel { fill: var(--panel); stroke: var(--panel-edge); stroke-width: 2; }
  .band { fill: var(--blue); }
  .rule { stroke: var(--blue); stroke-width: 3; }
  .strip { fill: var(--blue); }
  .brand-name {
    font-family: "Montserrat", sans-serif;
    font-weight: 800;
    fill: var(--ink);
    letter-spacing: -1px;
  }
  .strip-label {
    font-family: "Montserrat", sans-serif;
    font-weight: 500;
    fill: var(--white);
    letter-spacing: 1px;
  }
  .side-label {
    font-family: "Oswald", sans-serif;
    font-weight: 600;
    fill: var(--white);
    letter-spacing: 1px;
  }
  .side-brand {
    font-family: "Montserrat", sans-serif;
    font-weight: 800;
    fill: var(--blue-deep);
  }
</style>
</head>
<body>
<svg class="box-artwork" viewBox="0 0 1200 1200" xmlns="http://www.w3.org/2000/svg">
  <defs>
    <linearGradient id="steel" x1="0" y1="0" x2="1" y2="1">
      <stop offset="0" stop-color="#c9ccd1"/>
      <stop offset="1" stop-color="#6f747b"/>
    </linearGradient>
  </defs>

  <!-- Lid panel -->
  <g class="lid-panel" transform="translate(50 60)">
    <rect class="panel" x="0" y="0" width="760" height="280"/>
    <polygon class="band" points="560,280 760,280 760,150"/>
    <line class="rule" x1="0" y1="22" x2="760" y2="22"/>
    <text class="brand-name" x="380" y="80" font-size="50" text-anchor="middle">BoltCrest</text>
    <rect class="strip" x="0" y="94" width="760" height="42"/>
    <text class="strip-label" x="380" y="125" font-size="28" text-anchor="middle">SCREW &amp; NAIL</text>
    <line class="rule" x1="0" y1="146" x2="760" y2="146"/>
    <rect role="img" aria-label="Illustration of a nail and a countersunk screw"
          x="210" y="170" width="300" height="90" rx="16"
          fill="url(#steel)" opacity="0.85"/>
  </g>

  <!-- Front panel -->
  <g class="front-panel" transform="translate(50 340)">
    <rect class="panel" x="0" y="0" width="760" height="540"/>
    <polygon class="band" points="100,540 420,540 760,330 760,20"/>

    <text class="brand-name" x="30" y="110" font-size="80">BoltCrest</text>
    <line class="rule" x1="0" y1="138" x2="520" y2="138"/>
    <rect class="strip" x="0" y="150" width="500" height="66"/>
    <text class="strip-label" x="28" y="200" font-size="44">SCREW &amp; NAIL</text>
    <line class="rule" x1="0" y1="228" x2="470" y2="228"/>

    <rect role="img" aria-label="Illustration of a nail and a countersunk screw"
          x="320" y="325" width="320" height="110" rx="20"
          fill="url(#steel)" opacity="0.85"
          transform="rotate(-36 480 380)"/>
  </g>

  <!-- Side panel -->
  <g class="side-panel" transform="translate(810 340)">
    <rect class="panel" x="0" y="0" width="340" height="540"/>
    <polygon class="band" points="0,20 340,20 340,170 0,330"/>
    <text class="side-label" font-size="50" text-anchor="middle"
          transform="translate(170 150) rotate(-70)">
      <tspan x="0" y="-38">SCREW</tspan>
      <tspan x="0" y="17">AND</tspan>
      <tspan x="0" y="72">NAIL</tspan>
    </text>
    <line class="rule" x1="20" y1="522" x2="320" y2="382"/>
    <text class="side-brand" font-size="40"
          transform="translate(30 500) rotate(-25)">BoltCrest</text>
  </g>
</svg>
</body>
</html>
```